Business Card Design

My business is writing crime novels to entertain readers. I write legal thrillers and mysteries. I need a card for publishers, agents, other authors, and media.

Industry/Entity Type

Legal

Contact Information for Business Card

Paul Ostrander
www.ostranderthrillers.example
paulbostrander@mailbox.example
0064 27 5139427

```html
<!DOCTYPE html>
<html lang="en">
<head>
<meta charset="utf-8">
<title>Paul Ostrander – Business Card</title>
<link rel="stylesheet" href="https://fonts.googleapis.com/css2?family=Exo+2:wght@400;600&family=Tinos&display=swap">
<style>
  :root {
    --ink-blue: #2e3192;
    --card-white: #ffffff;
    --backdrop: #e9e6e1;
    --portrait-light: #9a9a9a;
    --portrait-dark: #6f6f6f;
  }
  html, body {
    margin: 0;
    padding: 0;
    width: 1200px;
    height: 870px;
    overflow: hidden;
    background: var(--backdrop);
  }
  .stage {
    width: 1200px;
    height: 870px;
    display: flex;
    align-items: center;
    justify-content: center;
  }
  .business-card {
    width: 450px;
    height: 788px;
    background: var(--card-white);
    box-shadow: 0 2px 10px rgba(0,0,0,0.12);
    box-sizing: border-box;
    padding: 40px 34px 0;
    display: flex;
    flex-direction: column;
    align-items: center;
    color: var(--ink-blue);
  }
  .portrait-frame {
    width: 382px;
    height: 372px;
    border: 11px solid var(--ink-blue);
    box-sizing: border-box;
  }
  .portrait-photo {
    width: 100%;
    height: 100%;
    background: radial-gradient(ellipse at 50% 35%, var(--portrait-light), var(--portrait-dark));
  }
  .holder-name {
    margin: 42px 0 0;
    font-family: "Exo 2", sans-serif;
    font-weight: 600;
    font-size: 33px;
    letter-spacing: 0.5px;
    line-height: 1;
    text-transform: uppercase;
  }
  .holder-role {
    margin: 4px 0 0;
    font-family: "Exo 2", sans-serif;
    font-weight: 400;
    font-size: 17px;
    letter-spacing: 1px;
    line-height: 1;
    text-transform: uppercase;
  }
  .contact-list {
    list-style: none;
    margin: 58px 0 0;
    padding: 0;
    text-align: center;
    font-family: "Tinos", serif;
    font-size: 19px;
    letter-spacing: 1.6px;
    line-height: 1.75;
  }
</style>
</head>
<body>
  <main class="stage">
    <article class="business-card">
      <div class="portrait-frame">
        <div class="portrait-photo" role="img" aria-label="Portrait photograph of Paul Ostrander in a leather jacket against a grey studio backdrop"></div>
      </div>
      <h1 class="holder-name">Paul Ostrander</h1>
      <p class="holder-role">Owaner</p>
      <ul class="contact-list">
        <li class="contact-phone">0064 27 5139427</li>
        <li class="contact-web">www.ostranderthrillers.example</li>
        <li class="contact-email">paulbostrander@mailbox.example</li>
      </ul>
    </article>
  </main>
</body>
</html>
```